Family Ranch with a hobby vineyard needs 2 wine labels for our first harvest

Design 2 wine labels (front and back) with the Brindor Ranch logo.
Label 1:
Sauvignon Blanc
Alc. 12.5% by Vol.
Palos Verdes Peninsula - add as the region
Year 2022
Label 2:
Cabernet Sauvignon
Alc. 13.5% by Vol.
Year 2022
For the back label design:
GOVERNMENT WARNING: (1) According to the Surgeon General, women
should not drink alcoholic beverages during pregnancy because of the risk of
birth defects. (2) Consumption of alcoholic beverages impairs your ability to
drive a car or operate machinery, and may cause health problems.
Contains Sulfates.
750ML
I just received the bottles and have attached a picture.
Look and feel
Each slider illustrates characteristics of the customer's brand and the style your logo design should communicate.

```html
<!DOCTYPE html>
<html lang="en">
<head>
<meta charset="utf-8">
<title>Brindor Ranch – Sauvignon Blanc Labels</title>
<link href="https://fonts.googleapis.com/css2?family=Montserrat:wght@300;400;500;700&display=swap" rel="stylesheet">
<style>
  :root {
    --page: #ffffff;
    --label-dark: #161616;
    --cream: #e8e1dc;
    --ink: #141414;
    --taupe: #7a6d6b;
    --dot: #9a8f8c;
  }
  * { box-sizing: border-box; margin: 0; padding: 0; }
  html, body { width: 1200px; height: 1200px; overflow: hidden; background: var(--page); }
  body { position: relative; font-family: "Montserrat", sans-serif; }

  .label { position: absolute; background: var(--label-dark); }
  .label--front { left: 169px; top: 239px; width: 412px; height: 729px; }
  .label--back  { left: 626px; top: 545px; width: 411px; height: 422px; }

  .brand { position: absolute; top: 46px; left: 0; width: 100%; text-align: center; color: var(--cream); font-family: "Montserrat", sans-serif; font-weight: 500; }
  .brand__name { display: block; font-size: 34px; letter-spacing: 1px; line-height: 1; }
  .brand__sub { display: block; font-size: 14px; letter-spacing: 7px; margin-top: 8px; padding-left: 7px; }

  .brand-mark { position: absolute; left: 86px; top: 180px; width: 240px; height: 240px; border-radius: 50%; border: 4px solid var(--cream); }

  .ticket { position: absolute; background: var(--cream); }
  .ticket::before, .ticket::after {
    content: ""; position: absolute; top: 4px; bottom: 4px; width: 8px;
    background: radial-gradient(circle, var(--label-dark) 2.6px, transparent 3.2px) 0 0 / 8px 9px repeat-y;
  }
  .ticket::before { left: -4px; }
  .ticket::after { right: -4px; }

  .ticket--front { left: 24px; top: 547px; width: 364px; height: 136px; padding: 22px 28px 0 30px; }
  .ticket--back  { left: 24px; top: 45px; width: 364px; height: 336px; padding: 22px 24px 0 30px; }

  .rule { height: 2px; background: radial-gradient(circle, var(--dot) 0.9px, transparent 1.2px) 0 0 / 6px 2px repeat-x; }

  .wine-name { font-weight: 700; font-size: 23px; letter-spacing: 2.6px; color: var(--ink); text-align: center; line-height: 1; }
  .ticket--front .rule { margin: 13px 2px 10px; }
  .region { font-weight: 400; font-size: 18px; letter-spacing: 1.8px; color: var(--ink); text-align: center; line-height: 1; }
  .specs { display: flex; justify-content: space-between; margin-top: 14px; font-weight: 700; font-size: 16px; letter-spacing: 0.6px; color: var(--taupe); }

  .warning-title { font-weight: 700; font-size: 17px; letter-spacing: 3.2px; color: var(--taupe); line-height: 1; }
  .warning-title span { font-weight: 400; }
  .warning-text { font-weight: 400; font-size: 14.5px; letter-spacing: 1.6px; line-height: 20px; color: var(--ink); margin-top: 9px; }
  .ticket--back .rule { margin: 12px 0 3px; }
  .ticket--back .rule--end { margin: 21px 0 10px; }
  .back-footer { display: flex; justify-content: space-between; font-size: 16px; color: var(--taupe); letter-spacing: 0.4px; }
  .back-footer .volume { font-weight: 700; }
  .back-footer .sulfites { font-weight: 400; }
</style>
</head>
<body>
  <section class="label label--front">
    <div class="brand">
      <span class="brand__name">BRINDOR</span>
      <span class="brand__sub">RANCH</span>
    </div>
    <div class="brand-mark" aria-hidden="true"></div>
    <div class="ticket ticket--front">
      <h1 class="wine-name">SAUVIGNON BLANC</h1>
      <div class="rule"></div>
      <p class="region">PALOS VERDES PENINSULA</p>
      <div class="specs">
        <span class="vintage">YEAR 2022</span>
        <span class="abv">12.5% VOL</span>
      </div>
    </div>
  </section>

  <section class="label label--back">
    <div class="ticket ticket--back">
      <h2 class="warning-title">GOVERNMENT WARNING<span>:</span></h2>
      <p class="warning-text">According to the Surgeon<br>General, women should not<br>drink alcoholic beverages during<br>pregnancy because of the risk<br>of birth defects.</p>
      <div class="rule"></div>
      <p class="warning-text">Consumption of alcoholic<br>beverages impairs your ability<br>to drive a car or operate<br>machinery, and may cause<br>health problems.</p>
      <div class="rule rule--end"></div>
      <div class="back-footer">
        <span class="volume">750ML</span>
        <span class="sulfites">CONTAINS SULFATES</span>
      </div>
    </div>
  </section>
</body>
</html>
```